Best in class business looking for best in class stationery that accurately reflects the brand image we are trying to build as the brand expands throughout the country. The Varying items should be an eye catching design that makes even the simplest letter or small business card stand out in the crowd.

Target Market(s)

Professionals

Industry/Entity Type

Real Estate

Other font styles liked:
• See atttached logo

Requirements
Must have
• Letterhead
• Business cards
• Envelopes
• Labels for larger mailings
Nice to have
• Folders
• Notebook
Should not have
• Stale design elements

```html
<!DOCTYPE html>
<html lang="pl">
<head>
<meta charset="utf-8">
<title>Ridgeline Property Group – stationery set</title>
<link rel="stylesheet" href="https://fonts.googleapis.com/css2?family=Lato:wght@400;700&display=swap">
<style>
  :root {
    --navy: #231f5e;
    --brand-blue: #2b3f9e;
    --lilac: #a3a8e0;
    --paper: #f4f4f6;
    --ink: #2a2a33;
    --rule: #c9c9d2;
    --backdrop: #e6e6ec;
  }
  * { box-sizing: border-box; margin: 0; padding: 0; }
  html, body { width: 1200px; height: 822px; overflow: hidden; }
  body {
    background: var(--backdrop);
    font-family: "Lato", sans-serif;
    color: var(--ink);
    position: relative;
  }
  .sheet {
    position: absolute;
    background: var(--paper);
    box-shadow: 0 2px 6px rgba(30, 30, 60, 0.12);
  }
  .sheet--banded { border-left: 18px solid var(--navy); }

  .brand-name {
    font-family: "Lato", sans-serif;
    font-weight: 700;
    color: var(--brand-blue);
    text-transform: uppercase;
    letter-spacing: 0.04em;
    display: flex;
    align-items: center;
    gap: 5px;
    line-height: 1;
  }
  .brand-name::before {
    content: "";
    width: 8px; height: 8px;
    background: var(--brand-blue);
    flex: none;
  }

  /* envelope front */
  .envelope-front { left: 86px; top: 170px; width: 402px; height: 192px; border-left-width: 12px; }
  .envelope-front .brand-name { position: absolute; left: 30px; top: 30px; font-size: 7px; }
  .recipient { position: absolute; left: 284px; top: 112px; font-size: 7px; line-height: 1.45; }
  .recipient strong { font-weight: 700; }

  /* envelope back */
  .envelope-back { position: absolute; left: 68px; top: 397px; width: 418px; height: 205px; }
  .envelope-back svg { display: block; }

  /* letterhead */
  .letterhead { left: 522px; top: 78px; width: 394px; height: 524px; border-left-width: 18px; }
  .letterhead .brand-name { position: absolute; left: 32px; top: 52px; font-size: 8px; }
  .letter-body { position: absolute; left: 32px; top: 132px; width: 310px; font-size: 6.6px; line-height: 1.5; }
  .letter-body p { margin-bottom: 9px; }
  .letter-body .salutation { margin-bottom: 11px; }
  .letter-footer { position: absolute; left: 32px; bottom: 38px; width: 270px; font-size: 4.6px; font-weight: 700; line-height: 1.4; }

  /* business cards */
  .card-front { left: 920px; top: 78px; width: 166px; height: 90px; }
  .card-front .brand-name { position: absolute; left: 50%; top: 42px; transform: translateX(-50%); font-size: 6.5px; white-space: nowrap; }

  .card-back { left: 928px; top: 202px; width: 170px; height: 90px; border-left-width: 7px; }
  .card-holder { position: absolute; left: 12px; top: 22px; }
  .card-holder .person { font-size: 8px; line-height: 1.2; color: var(--ink); }
  .card-holder .role { font-size: 3.6px; font-weight: 700; letter-spacing: 0.04em; margin-top: 4px; }
  .card-holder .contact { font-size: 3.6px; margin-top: 9px; line-height: 1.4; }
  .card-mark { position: absolute; right: 8px; bottom: 8px; width: 30px; height: 30px; background: var(--brand-blue); }

  /* notepad */
  .notepad { left: 936px; top: 420px; width: 196px; height: 182px; }
  .notepad .brand-name { position: absolute; left: 50%; top: 20px; transform: translateX(-50%); font-size: 5.5px; white-space: nowrap; }
  .note-lines { position: absolute; left: 20px; right: 20px; top: 42px; }
  .note-lines span { display: block; height: 11.8px; border-bottom: 1px solid var(--rule); }
  .notepad-footer { position: absolute; left: 28px; right: 28px; bottom: 12px; font-size: 3px; line-height: 1.4; text-align: center; }
</style>
</head>
<body>

  <section class="sheet sheet--banded envelope-front" aria-label="Envelope, front">
    <div class="brand-name">Ridgeline Property Group</div>
    <address class="recipient">
      Szanowny Pan/Pani<br>
      <strong>Marta Nowicka</strong><br>
      62-118 Lipowo<br>
      ul. Spokojna 14/2
    </address>
  </section>

  <section class="envelope-back" aria-label="Envelope, back">
    <svg width="418" height="205" viewBox="0 0 418 205">
      <rect x="0" y="0" width="418" height="205" fill="var(--navy)"/>
      <path d="M26 40 Q26 50 36 50 H390 Q400 50 400 40 V68 H26 Z" fill="var(--lilac)"/>
      <path d="M18 68 H408 V86 Q408 95 398 95 H28 Q18 95 18 86 Z" fill="var(--paper)"/>
      <rect x="42" y="156" width="12" height="12" fill="#2e2a72"/>
    </svg>
  </section>

  <section class="sheet sheet--banded letterhead" aria-label="Letterhead">
    <div class="brand-name">Ridgeline Property Group</div>
    <div class="letter-body">
      <p class="salutation">Lorem ipsum</p>
      <p>Dolor sit amet, consectetur adipiscing elit. Curabitur ultrices congue orci ac malesuada. Nam posuere arcu magna, at placerat nisl tempus nec. Phasellus suscipit sapien quis tempus convallis. Vestibulum aliquam eros nec diam viverra, tempor euismod nunc dapibus. Donec ultricies metus a ipsum viverra vestibulum. Duis vel aliquet velit. Quisque commodo odio eu turpis rhoncus tincidunt. Aliquam sit amet neque arcu. Aenean sed arcu nec ligula posuere venenatis. Pellentesque vitae magna elementum, tincidunt dolor et, porttitor ligula. Quisque vestibulum dapibus tellus. Aliquam leo ante, scelerisque sit amet lacinia sed, laoreet ac tortor. Cras id commodo dolor. Sed placerat interdum vehicula. Maecenas imperdiet rhoncus dui ut varius.</p>
      <p>Duis mollis varius sagittis. Vestibulum ante ipsum primis in faucibus orci luctus et ultrices posuere cubilia Curae; Maecenas ullamcorper varius diam, ac malesuada est. Sed accumsan odio et mi laoreet, in aliquam ante tempor. Praesent ut rhoncus nibh. Ut vel sodales enim, ac tempor nisl. Suspendisse convallis malesuada leo, et hendrerit risus lobortis vitae. Suspendisse consectetur purus sed mauris vehicula, pellentesque vehicula risus blandit. Quisque ut velit vulputate, placerat elit id, tincidunt lectus. Aenean vel justo iaculis, rutrum metus non, faucibus mi. Maecenas mauris dolor, posuere venenatis auctor eu, fermentum vitae libero. Mauris sit amet condimentum tellus. Ut et dapibus ante, eu tincidunt lorem. Curabitur iaculis eros et libero posuere varius. Vivamus vel lacus erat.</p>
      <p>Aliquam in ante nec sapien commodo varius. Vivamus sit amet venenatis augue. Aliquam vitae orci nulla. Proin non molestie lacus. Fusce eu pulvinar dolor. Nullam metus enim, pulvinar sed velit nec, pulvinar viverra metus. Pellentesque lacinia, arcu condimentum pulvinar rutrum, massa tortor porttitor tortor, eu elementum eros nisi id neque. Phasellus accumsan ligula fermentum, dignissim arcu non, tristique mauris. Curabitur scelerisque metus tortor, at dapibus urna gravida quis. Vivamus sed dolor elit. Nulla fermentum laoreet urna, sed aliquam risus lobortis nec. Aliquam sed cursus nunc, et sollicitudin nunc.</p>
    </div>
    <p class="letter-footer">Lorem ipsum dolor sit amet, consectetur adipiscing elit. Curabitur ultrices congue orci ac malesuada. Nam posuere arcu tempus nec. Phasellus suscipit sapien quis tempus convallis. Vestibulum</p>
  </section>

  <section class="sheet card-front" aria-label="Business card, front">
    <div class="brand-name">Ridgeline Property Group</div>
  </section>

  <section class="sheet sheet--banded card-back" aria-label="Business card, back">
    <div class="card-holder">
      <p class="person">Marta<br>Nowicka</p>
      <p class="role">STARSZA BRYGADZISTKA</p>
      <p class="contact">m.nowicka@rpg.pl<br>481 207 935</p>
    </div>
    <div class="card-mark"></div>
  </section>

  <section class="sheet notepad" aria-label="Notepad">
    <div class="brand-name">Ridgeline Property Group</div>
    <div class="note-lines">
      <span></span><span></span><span></span><span></span><span></span>
      <span></span><span></span><span></span><span></span><span></span><span></span>
    </div>
    <p class="notepad-footer">Ridgeline Property Group, 14 Spokojna Street, Lipowo. Notes for daily property visits and client meetings.</p>
  </section>

</body>
</html>
```